Carrow Building Partners Website

Need a dynamic corporate website that can be built on with time. We want to get our information out to the world and have a place where customers can submit requests for proposals.

Target Market(s)

Custom home owners and buyers. Architects and Real Estate Agents.

Industry/Entity Type

Construction

Number of Pages Required

3 page

Font styles to use
Serif
Sans Serif

Requirements
Must have
• Company logo, about, company contact information, biography, contact, projects,
• Sleek, modern, clean, attractive design.
• Online form customers can use for filling out a request for project proposal.
• Linkedin hyperlink.
• Uses www.carrowbuildingpartners.com

```html
<!DOCTYPE html>
<html lang="en">
<head>
<meta charset="utf-8">
<title>Carrow Building Partners</title>
<link href="https://fonts.googleapis.com/css2?family=Montserrat:wght@400;600;700;800&family=Open+Sans:ital,wght@0,400;0,600;0,700;1,400&display=swap" rel="stylesheet">
<style>
:root{
  --navy:#16306b;
  --blue:#1f4f9c;
  --blue-light:#3b7ad1;
  --ink:#1d2433;
  --gray:#6b7280;
  --line:#c9ced8;
  --paper:#ffffff;
  --mist:#eef0f4;
}
*{margin:0;padding:0;box-sizing:border-box}
html,body{width:1200px;height:2728px;overflow:hidden;background:var(--paper)}
body{position:relative;font-family:"Open Sans",Arial,sans-serif;color:var(--ink)}
.abs{position:absolute}
.head-font{font-family:"Montserrat",Arial,sans-serif}

/* header */
.site-header{position:absolute;left:0;top:0;width:1200px;height:104px;background:var(--paper)}
.brand{position:absolute;left:24px;top:28px;display:flex;align-items:center;gap:14px}
.brand-square{width:44px;height:44px;background:var(--blue)}
.brand-name{font-family:"Montserrat",sans-serif;font-weight:800;font-size:28px;color:var(--blue);letter-spacing:.5px}
.connect-tab{position:absolute;right:40px;top:0;height:26px;padding:0 14px;background:var(--navy);color:#fff;font-size:12px;font-weight:700;display:flex;align-items:center;gap:8px;letter-spacing:1px}
.connect-tab i{width:14px;height:14px;border-radius:50%;background:#fff;display:block}
.header-contact{position:absolute;right:40px;top:56px;display:flex;gap:32px;font-size:16px;font-weight:600;color:var(--ink)}
.header-contact span{display:flex;align-items:center;gap:8px}

/* nav */
.main-nav{position:absolute;left:0;top:104px;width:1200px;height:48px;background:var(--blue);display:flex;justify-content:space-around;align-items:stretch}
.main-nav a{color:#fff;text-decoration:none;font-family:"Montserrat",sans-serif;font-weight:600;font-size:16px;letter-spacing:1px;display:flex;align-items:center;padding:0 28px}
.main-nav a.active{background:var(--blue-light)}

/* hero */
.hero{position:absolute;left:0;top:152px;width:1200px;height:488px;background:linear-gradient(180deg,#8fb0d6 0%,#c9d6e4 35%,#6d6a66 70%,#2e3a2a 100%)}
.hero-caption{position:absolute;left:0;bottom:0;width:100%;height:60px;background:rgba(10,22,50,.78);display:flex;align-items:center;justify-content:space-between;padding:0 40px}
.hero-caption p{color:#fff;font-family:"Montserrat",sans-serif;font-weight:700;font-size:25px}
.hero-caption .tag{color:#fff;font-family:"Montserrat",sans-serif;font-weight:800;font-size:18px;display:flex;align-items:center;gap:8px}
.hero-caption .tag i{width:20px;height:20px;background:#fff;display:block}

/* section titles */
.section-title{position:absolute;left:0;width:1200px;display:flex;justify-content:center;align-items:center;gap:20px;font-family:"Montserrat",sans-serif;font-weight:800;font-size:34px;letter-spacing:1px}
.section-title::before,.section-title::after{content:"";width:110px;height:2px;background:currentColor;opacity:.5}
.section-sub{position:absolute;left:0;width:1200px;text-align:center}

/* welcome */
.welcome-title{top:666px;color:var(--ink)}
.welcome-title b{color:var(--blue);font-size:28px;display:flex;align-items:center;gap:8px}
.welcome-title b i{width:26px;height:26px;background:var(--blue);display:block}
.welcome-sub{top:724px;font-size:20px;font-style:italic;color:var(--gray)}
.team-photo{position:absolute;left:80px;top:820px;width:480px;height:200px;background:linear-gradient(135deg,#cfd8e2,#f1f2f4 45%,#e8c466 70%,#b8c3cf)}
.about-text{position:absolute;left:80px;top:1036px;width:480px;font-size:12.5px;line-height:1.7;color:var(--gray)}
.services-head{position:absolute;left:592px;top:834px;font-family:"Montserrat",sans-serif;font-weight:800;font-size:22px;color:var(--blue)}
.services{position:absolute;left:592px;top:894px;width:560px;display:grid;grid-template-columns:1fr 1fr;row-gap:36px;column-gap:30px}
.service{display:flex;gap:14px}
.service-icon{flex:0 0 44px;height:44px;border-radius:50%;background:var(--blue);display:flex;align-items:center;justify-content:center}
.service h3{font-family:"Montserrat",sans-serif;font-weight:700;font-size:19px;color:var(--blue);margin-bottom:6px}
.service p{font-size:12px;line-height:1.5;color:var(--gray)}

/* why choose */
.why{position:absolute;left:0;top:1160px;width:1200px;height:580px;background:linear-gradient(160deg,#1c3f86 0%,#16306b 55%,#0f2456 100%)}
.why-title{top:112px;color:#fff}
.why-sub{top:196px;color:#9cc0f0;font-size:19px;font-style:italic}
.feature{position:absolute;width:330px;color:#fff}
.feature h4{font-family:"Montserrat",sans-serif;font-weight:700;font-size:21px;margin-bottom:6px}
.feature p{font-size:12.5px;line-height:1.5;color:#c7d4ee}
.feature.left{text-align:left}
.feature-dot{position:absolute;width:34px;height:34px;border-radius:50%;border:2px solid #fff;display:flex;align-items:center;justify-content:center}
.feature-line{position:absolute;height:2px;background:rgba(255,255,255,.45)}
.why-center{position:absolute;left:480px;top:200px;width:240px;height:240px;display:flex;flex-direction:column;align-items:center;justify-content:center;gap:14px}
.why-center i{width:120px;height:120px;background:rgba(255,255,255,.18);display:block}
.why-center span{font-family:"Montserrat",sans-serif;font-weight:800;font-size:18px;color:#fff;text-align:center}

/* projects */
.projects-title{top:1790px;color:var(--blue)}
.projects-sub{top:1850px;font-family:"Montserrat",sans-serif;font-weight:700;font-size:20px;color:var(--ink)}
.tile{position:absolute}
.arrow{position:absolute;top:2056px;font-size:36px;color:var(--gray);font-family:"Montserrat",sans-serif}

/* contact */
.contact{position:absolute;left:0;top:2300px;width:1200px;height:372px;background:var(--mist)}
.contact-title{top:2334px;color:var(--blue)}
.form-lead{position:absolute;left:80px;top:2410px;font-weight:600;font-size:17px;color:var(--ink)}
.field{position:absolute;background:#fff;border:1px solid var(--line);font-size:13px;color:var(--gray);padding:8px 12px}
.submit{position:absolute;left:420px;top:2574px;width:80px;height:32px;background:var(--blue);color:#fff;font-weight:700;font-size:14px;display:flex;align-items:center;justify-content:center}
.info{position:absolute;left:812px;width:340px}
.info h5{font-family:"Montserrat",sans-serif;font-weight:700;font-size:17px;color:var(--navy);margin-bottom:4px;display:flex;align-items:center;gap:10px}
.info p{font-size:13px;line-height:1.55;color:var(--gray);padding-left:28px}
.info p.big{font-size:22px;color:var(--navy);font-weight:600}

/* footer */
.site-footer{position:absolute;left:0;top:2672px;width:1200px;height:56px;background:var(--navy);color:#fff;display:flex;justify-content:space-between;align-items:center;padding:0 40px;font-size:13px}
.site-footer span{display:flex;align-items:center;gap:10px}
.site-footer i{width:22px;height:22px;border-radius:50%;background:#fff;display:block}
</style>
</head>
<body>

<header class="site-header">
  <div class="brand"><div class="brand-square"></div><div class="brand-name">CARROW BUILDING PARTNERS</div></div>
  <div class="connect-tab">CONNECT US <i></i></div>
  <div class="header-contact">
    <span><svg width="18" height="18" viewBox="0 0 24 24"><circle cx="12" cy="12" r="12" fill="#1f4f9c"/><path d="M8 6l2 0 1 3-1.5 1a7 7 0 0 0 3.5 3.5l1-1.5 3 1 0 2c0 1-1 2-2 2A10 10 0 0 1 6 8c0-1 1-2 2-2z" fill="#fff"/></svg>555 010 2468</span>
    <span><svg width="18" height="18" viewBox="0 0 24 24"><circle cx="12" cy="12" r="12" fill="#1f4f9c"/><rect x="6" y="8" width="12" height="8" fill="none" stroke="#fff" stroke-width="1.5"/><path d="M6 8l6 5 6-5" fill="none" stroke="#fff" stroke-width="1.5"/></svg>info@carrowbuildingpartners.com</span>
  </div>
</header>

<nav class="main-nav">
  <a class="active" href="#">HOME</a><a href="#">ABOUT US</a><a href="#">SERVICES</a><a href="#">GALLERY</a><a href="#">CONTACT US</a>
</nav>

<section class="hero" role="img" aria-label="Modern two-storey custom home with stone walls and large lit windows at dusk">
  <div class="hero-caption">
    <p>Carrow Building is Turn-Key Construction Management Services Provider</p>
    <div class="tag"><i></i>CARROW</div>
  </div>
</section>

<h2 class="section-title welcome-title">WELCOME TO <b><i></i>CARROW</b></h2>
<p class="section-sub welcome-sub">Lorem ipsum dolor sit amet, consectetuer Lorem ipsum dolor sit amet adipiscing</p>

<div class="team-photo" role="img" aria-label="Team of builders in hard hats on a job site"></div>
<p class="about-text">We plan, manage and build custom homes from first sketch to final walkthrough. Our crews work closely with owners, architects and agents so every project stays on schedule, on budget and true to the design. Ask us for a proposal and we will answer within two days.</p>

<h3 class="services-head">WE PROVIDE SERVICES IN</h3>
<div class="services">
  <div class="service"><div class="service-icon"><svg width="22" height="22" viewBox="0 0 24 24"><circle cx="12" cy="12" r="4" fill="none" stroke="#fff" stroke-width="2"/><path d="M12 2v4M12 18v4M2 12h4M18 12h4" stroke="#fff" stroke-width="2"/></svg></div><div><h3>Engineering</h3><p>Structural plans and site studies for each custom build.</p></div></div>
  <div class="service"><div class="service-icon"><svg width="22" height="22" viewBox="0 0 24 24"><path d="M4 20l4-1 11-11-3-3L5 16z" fill="#fff"/></svg></div><div><h3>Design</h3><p>Layouts shaped around your lot, style and budget.</p></div></div>
  <div class="service"><div class="service-icon"><svg width="22" height="22" viewBox="0 0 24 24"><path d="M3 12l9-8 9 8v8H3z" fill="#fff"/></svg></div><div><h3>Construction</h3><p>Skilled crews building with care from slab to roof.</p></div></div>
  <div class="service"><div class="service-icon"><svg width="22" height="22" viewBox="0 0 24 24"><rect x="4" y="12" width="4" height="8" fill="#fff"/><rect x="10" y="8" width="4" height="12" fill="#fff"/><rect x="16" y="4" width="4" height="16" fill="#fff"/></svg></div><div><h3>Management</h3><p>Clear schedules, costs and updates at every stage.</p></div></div>
</div>

<section class="why">
  <h2 class="section-title why-title">WHY CHOOSE US</h2>
  <p class="section-sub why-sub">We Are A Leading Construction Management &amp; Engineering Company</p>

  <div class="feature left" style="left:100px;top:288px"><h4>Certified Experience</h4><p>Licensed builders with decades on custom homes.</p></div>
  <div class="feature-line" style="left:350px;top:318px;width:130px"></div>
  <div class="feature-dot" style="left:330px;top:286px"><svg width="16" height="16" viewBox="0 0 24 24"><circle cx="12" cy="10" r="6" fill="#fff"/><path d="M8 15l-2 7 6-3 6 3-2-7" fill="#fff"/></svg></div>

  <div class="feature left" style="left:100px;top:428px"><h4>Competitive Pricing</h4><p>Fair, open quotes with no hidden costs later.</p></div>
  <div class="feature-line" style="left:350px;top:458px;width:130px"></div>
  <div class="feature-dot" style="left:330px;top:426px"><svg width="16" height="16" viewBox="0 0 24 24"><path d="M12 3v18M16 7H10a3 3 0 0 0 0 6h4a3 3 0 0 1 0 6H8" fill="none" stroke="#fff" stroke-width="2"/></svg></div>

  <div class="why-center"><i></i><span>CARROW BUILDING PARTNERS</span></div>

  <div class="feature-line" style="left:720px;top:318px;width:100px"></div>
  <div class="feature-dot" style="left:786px;top:286px"><svg width="16" height="16" viewBox="0 0 24 24"><circle cx="12" cy="8" r="4" fill="#fff"/><path d="M4 21a8 8 0 0 1 16 0z" fill="#fff"/></svg></div>
  <div class="feature" style="left:836px;top:288px"><h4>Highly Professionals</h4><p>Trained teams who respect your home and time.</p></div>

  <div class="feature-line" style="left:720px;top:458px;width:100px"></div>
  <div class="feature-dot" style="left:786px;top:426px"><svg width="16" height="16" viewBox="0 0 24 24"><path d="M5 12l5 5 9-10" fill="none" stroke="#fff" stroke-width="3"/></svg></div>
  <div class="feature" style="left:836px;top:428px"><h4>100% Satisfaction</h4><p>We finish only when you are fully happy.</p></div>
</section>

<h2 class="section-title projects-title">OUR PROJECTS</h2>
<p class="section-sub projects-sub">Lorem ipsum dolor sit amet, consectetuer Lorem ipsum dolor sit amet</p>

<div class="arrow" style="left:26px">&#8249;</div>
<div class="arrow" style="left:1158px">&#8250;</div>

<div class="tile" role="img" aria-label="Project video showing a builder at work" style="left:80px;top:1920px;width:308px;height:300px;background:linear-gradient(160deg,#5a4a3c,#2a2420)">
  <svg class="abs" style="left:124px;top:120px" width="60" height="60" viewBox="0 0 60 60"><circle cx="30" cy="30" r="28" fill="rgba(255,255,255,.85)"/><path d="M24 18l18 12-18 12z" fill="#1d2433"/></svg>
  <div class="abs" style="left:0;bottom:0;width:100%;height:22px;background:rgba(0,0,0,.6)"></div>
  <div class="abs" style="left:40px;bottom:9px;width:200px;height:4px;background:#3b7ad1"></div>
</div>
<div class="tile" role="img" aria-label="Builder reviewing plans on site" style="left:400px;top:1920px;width:196px;height:146px;background:linear-gradient(135deg,#d9b45a,#8a7456)"></div>
<div class="tile" role="img" aria-label="Construction team in hard hats" style="left:400px;top:2074px;width:196px;height:146px;background:linear-gradient(135deg,#a9b6c6,#d8a94e)"></div>
<div class="tile" role="img" aria-label="Finished suburban family home" style="left:604px;top:1920px;width:296px;height:146px;background:linear-gradient(180deg,#a9c3e0,#b59a80 60%,#6b8a52)"></div>
<div class="tile" role="img" aria-label="Workers discussing a building project" style="left:604px;top:2074px;width:296px;height:146px;background:linear-gradient(135deg,#e4c35a,#c7ccd4 60%,#8f96a3)"></div>
<div class="tile" role="img" aria-label="Curved wooden staircase interior" style="left:908px;top:1920px;width:212px;height:300px;background:linear-gradient(160deg,#efe6da,#9a5f35 60%,#5a3620)"></div>

<section class="contact"></section>
<h2 class="section-title contact-title">CONTACT US</h2>
<p class="form-lead">Please Fill Your Details We Will Get Back to You Soon</p>
<div class="field" style="left:80px;top:2450px;width:320px;height:34px">Name</div>
<div class="field" style="left:80px;top:2496px;width:320px;height:34px">Email</div>
<div class="field" style="left:80px;top:2542px;width:320px;height:34px">Phone</div>
<div class="field" style="left:420px;top:2450px;width:290px;height:110px">How We Can Help You?</div>
<div class="submit">Submit</div>

<div class="info" style="top:2408px">
  <h5><svg width="18" height="18" viewBox="0 0 24 24"><path d="M12 2a7 7 0 0 0-7 7c0 5 7 13 7 13s7-8 7-13a7 7 0 0 0-7-7z" fill="#1f4f9c"/><circle cx="12" cy="9" r="2.5" fill="#fff"/></svg>ADDRESS INFORMATION</h5>
  <p>1171 Harbor Lane, Suite 200<br>Westfield, CA 90210</p>
</div>
<div class="info" style="top:2494px">
  <h5><svg width="18" height="18" viewBox="0 0 24 24"><rect x="3" y="6" width="18" height="12" fill="#1f4f9c"/><path d="M3 6l9 7 9-7" fill="none" stroke="#fff" stroke-width="1.5"/></svg>EMAIL</h5>
  <p>info@carrowbuildingpartners.com</p>
</div>
<div class="info" style="top:2566px">
  <h5><svg width="18" height="18" viewBox="0 0 24 24"><path d="M6 3l4 0 1 5-2 1.5a10 10 0 0 0 5.5 5.5L16 13l5 1 0 4c0 1.5-1.5 3-3 3A16 16 0 0 1 3 6c0-1.5 1.5-3 3-3z" fill="#1f4f9c"/></svg>CALL US</h5>
  <p class="big">555 010 2468</p>
</div>

<footer class="site-footer">
  <span>Copyright © 2016 Carrow Building Partners Inc. All Rights Reserved.</span>
  <span>Connect To <i></i></span>
</footer>

</body>
</html>
```